Security Warning Sign

We have an existing sign that needs an update. I have attached a picture of the current square sign. We need to maintain the same wording. It needs to be professional and appropriate to attach to our customers fence. Also attached is a copy of our building sign which may lend some inspiration and hopefully the ai format will assist. The final sign will be 600mm x 600mmOur website is www.halvorngate.com.au

```html
<!DOCTYPE html>
<html lang="en">
<head>
<meta charset="utf-8">
<title>Security Warning Sign – Halvorngate Security Services</title>
<link rel="stylesheet" href="https://fonts.googleapis.com/css2?family=Anton&family=Arimo:wght@700&display=swap">
<style>
  :root {
    --backdrop: #6b5b58;
    --sign-black: #0d0d0d;
    --sign-yellow: #eef57c;
    --warning-red: #ec1c1c;
    --accent-orange: #f47a1f;
    --ink: #0a0a0a;
    --white: #ffffff;
    --camera-dark: #2a2a2a;
    --camera-mid: #4a4a4a;
  }
  * { margin: 0; padding: 0; box-sizing: border-box; }
  html, body {
    width: 1200px; height: 1200px; overflow: hidden;
    background: var(--backdrop);
  }
  .canvas { position: relative; width: 1200px; height: 1200px; }

  .sign {
    position: absolute; left: 336px;
    width: 526px; height: 526px;
    background: var(--sign-black);
    border-radius: 34px;
    font-family: "Arimo", Arial, sans-serif;
    font-weight: 700;
    color: var(--ink);
  }
  .sign--red { top: 26px; }
  .sign--yellow { top: 654px; }

  .sign__header {
    position: absolute; left: 0; top: 0; width: 100%; height: 138px;
    display: flex; align-items: center; justify-content: center;
  }
  .sign__headline {
    font-family: "Anton", Impact, sans-serif;
    font-weight: 400;
    font-size: 98px; line-height: 1;
    letter-spacing: 1px;
    padding-top: 6px;
  }
  .sign--red .sign__headline { color: var(--warning-red); }
  .sign--yellow .sign__headline { color: var(--sign-yellow); }

  .sign__panel {
    position: absolute; left: 8px; right: 8px; top: 138px; bottom: 8px;
    background: var(--sign-yellow);
    border-radius: 0 0 28px 28px;
    overflow: hidden;
  }

  .sign__line {
    position: absolute; white-space: nowrap; line-height: 1;
    font-size: 38px;
  }
  /* positions relative to the panel (sign offset minus 8 / 138) */
  .line-1 { left: 21px; top: 8px; }
  .line-2 { left: 21px; top: 60px; }
  .line-3 { left: 16px; top: 109px; }
  .line-4 { left: 14px; top: 164px; }
  .line-5 { left: 12px; top: 202px; font-size: 70px; }

  .sign__camera {
    position: absolute; left: 350px; top: 4px;
    width: 161px; height: 114px;
    background: linear-gradient(160deg, var(--camera-mid), var(--camera-dark));
    border-radius: 14px;
  }

  .brand {
    position: absolute; left: 170px; top: 274px;
    display: flex; align-items: center; gap: 6px;
  }
  .brand__mark {
    width: 76px; height: 76px; border-radius: 50%;
    background: var(--accent-orange);
  }
  .brand__name {
    font-size: 19px; line-height: 20px; color: var(--ink);
  }

  .sign__web {
    position: absolute; left: 106px; top: 362px;
    font-size: 12px; line-height: 1; letter-spacing: 0.2px;
  }
  .sign__phone {
    position: absolute; right: 0; bottom: 0;
    width: 180px; height: 34px;
  }
  .sign__phone svg { position: absolute; inset: 0; }
  .sign__phone-text {
    position: absolute; left: 30px; top: 0; height: 34px;
    display: flex; align-items: center; gap: 6px;
    color: var(--white); font-size: 15px; line-height: 1;
  }
</style>
</head>
<body>
<div class="canvas">

  <section class="sign sign--red">
    <header class="sign__header"><h1 class="sign__headline">WARNING</h1></header>
    <div class="sign__panel">
      <p class="sign__line line-1">ELECTRONIC</p>
      <p class="sign__line line-2">SURVEILLANCE</p>
      <p class="sign__line line-3">AND RECORDING</p>
      <p class="sign__line line-4">DEVICES INSTALLED</p>
      <p class="sign__line line-5">IN THIS AREA</p>
      <div class="sign__camera" role="img" aria-label="Illustration of a wall-mounted CCTV camera"></div>
      <div class="brand">
        <span class="brand__mark"></span>
        <p class="brand__name">HALVORNGATE<br>SECURITY<br>SERVICES</p>
      </div>
      <p class="sign__web">WWW.HALVORNGATE.COM.AU</p>
      <div class="sign__phone">
        <svg viewBox="0 0 180 34" width="180" height="34" aria-hidden="true">
          <polygon points="14,0 180,0 180,34 0,34" fill="var(--accent-orange)"/>
        </svg>
        <span class="sign__phone-text">
          <svg width="14" height="14" viewBox="0 0 24 24" aria-hidden="true"><path fill="#fff" d="M6.6 10.8a15.1 15.1 0 0 0 6.6 6.6l2.2-2.2a1 1 0 0 1 1-.25 11.4 11.4 0 0 0 3.6.57 1 1 0 0 1 1 1V20a1 1 0 0 1-1 1A17 17 0 0 1 3 4a1 1 0 0 1 1-1h3.5a1 1 0 0 1 1 1c0 1.25.2 2.45.57 3.57a1 1 0 0 1-.25 1z"/></svg>
          1300 555 014
        </span>
      </div>
    </div>
  </section>

  <section class="sign sign--yellow">
    <header class="sign__header"><h1 class="sign__headline">WARNING</h1></header>
    <div class="sign__panel">
      <p class="sign__line line-1">ELECTRONIC</p>
      <p class="sign__line line-2">SURVEILLANCE</p>
      <p class="sign__line line-3">AND RECORDING</p>
      <p class="sign__line line-4">DEVICES INSTALLED</p>
      <p class="sign__line line-5">IN THIS AREA</p>
      <div class="sign__camera" role="img" aria-label="Illustration of a wall-mounted CCTV camera"></div>
      <div class="brand">
        <span class="brand__mark"></span>
        <p class="brand__name">HALVORNGATE<br>SECURITY<br>SERVICES</p>
      </div>
      <p class="sign__web">WWW.HALVORNGATE.COM.AU</p>
      <div class="sign__phone">
        <svg viewBox="0 0 180 34" width="180" height="34" aria-hidden="true">
          <polygon points="14,0 180,0 180,34 0,34" fill="var(--accent-orange)"/>
        </svg>
        <span class="sign__phone-text">
          <svg width="14" height="14" viewBox="0 0 24 24" aria-hidden="true"><path fill="#fff" d="M6.6 10.8a15.1 15.1 0 0 0 6.6 6.6l2.2-2.2a1 1 0 0 1 1-.25 11.4 11.4 0 0 0 3.6.57 1 1 0 0 1 1 1V20a1 1 0 0 1-1 1A17 17 0 0 1 3 4a1 1 0 0 1 1-1h3.5a1 1 0 0 1 1 1c0 1.25.2 2.45.57 3.57a1 1 0 0 1-.25 1z"/></svg>
          1300 555 014
        </span>
      </div>
    </div>
  </section>

</div>
</body>
</html>
```